Plumbing Company trying to attract new client base for particular works

In need of something to letterbox drop. There is an opportunity to provide "new sewer drains to the new sewer connections on your street".
There will be discounts for pensioners.
We have reviews from clients that are highly satisfied with our work.
Work booked within 1 months of stamped date on flyer will receive a further 10% off.
All work carried out by licences tradespeople.

LOGO will need to be altered to say "tidewell plumbing" rather than contracting

Target Market(s)

Home owners in regional South Australia - age 30+

Industry/Entity Type

It Company

Requirements
Must have
• contact phone number, email, company name,
Nice to have
• images,

```html
<!DOCTYPE html>
<html lang="en">
<head>
<meta charset="utf-8">
<title>Tidewell Plumbing – Letterbox Flyer</title>
<link href="https://fonts.googleapis.com/css2?family=Anton&family=Arimo:wght@400;700&family=Lato:wght@400;700;900&display=swap" rel="stylesheet">
<style>
  :root{
    --page-bg:#e9e6e1;
    --ink:#1b1b1b;
    --panel:#111111;
    --yellow:#f6d21e;
    --white:#ffffff;
    --grey:#8c8c8c;
    --text-dark:#222222;
  }
  *{box-sizing:border-box;margin:0;padding:0}
  html,body{width:902px;height:1200px;overflow:hidden;background:var(--page-bg)}
  .flyer{position:absolute;left:85px;top:75px;width:745px;height:1035px;background:var(--panel);overflow:hidden}
  .header{position:absolute;left:0;top:0;width:745px;height:112px;background:var(--white)}
  .brand{position:absolute;left:37px;top:20px;display:flex;align-items:center;gap:20px}
  .brand-mark{width:70px;height:70px;background:var(--yellow)}
  .brand-name{font-family:'Lato',sans-serif;font-weight:900;color:var(--ink);text-transform:uppercase;line-height:1}
  .brand-name .line1{display:block;font-size:32px;letter-spacing:1px}
  .brand-name .line2{display:block;font-size:18px;letter-spacing:5px;margin-top:6px}
  .social{position:absolute;right:30px;top:52px;display:flex;gap:13px}
  .social span{width:28px;height:28px;border-radius:4px;background:#4a8bc9}
  .header-rule{position:absolute;left:0;top:108px}
  .hero-photo{position:absolute;left:0;top:115px;width:745px;height:405px;
    background:linear-gradient(100deg,#6b4a3e 0%,#7d5a4c 30%,#b8443a 42%,#3a3a3a 55%,#8e9aa4 75%,#c9d1d6 100%)}
  .hero-rule{position:absolute;left:0;top:518px;width:745px;height:6px;background:var(--yellow)}
  .headline{position:absolute;left:23px;top:538px;font-family:'Anton',sans-serif;color:var(--white);font-size:35px;line-height:43px;letter-spacing:.3px}
  .headline .accent{display:block;color:var(--yellow);font-size:62px;line-height:76px;margin-top:2px}
  .offer-bar{position:absolute;left:15px;top:720px;width:410px;height:40px;
    background:linear-gradient(90deg,#c9c9c9,#ffffff 60%,#e6e6e6);
    clip-path:polygon(0 0,100% 0,92% 100%,0 100%);
    font-family:'Arimo',sans-serif;font-weight:700;font-size:23px;color:var(--text-dark);padding:6px 0 0 17px}
  .booking{position:absolute;left:30px;top:778px;font-family:'Lato',sans-serif;font-weight:700;color:var(--white);font-size:20px;line-height:30px}
  .booking .accent{color:var(--yellow);font-size:23px}
  .reviews{position:absolute;left:30px;top:852px;font-family:'Anton',sans-serif;color:var(--yellow);font-size:23px;line-height:32px;letter-spacing:.4px}
  .tile{position:absolute;width:155px;height:155px;border:6px solid var(--white);border-radius:8px;transform:rotate(45deg);overflow:hidden}
  .tile-trench{left:558px;top:444px;background:linear-gradient(135deg,#6e5a48,#3b3128)}
  .tile-pipe{left:444px;top:597px;background:linear-gradient(135deg,#8c7561,#5a4a3d)}
  .tile-tap{left:677px;top:582px;background:linear-gradient(135deg,#9aa0a4,#2b2b2b)}
  .tile-sprinkler{left:573px;top:742px;background:linear-gradient(135deg,#c8cfc4,#4d6b3c)}
  .contact-band{position:absolute;left:0;top:937px;width:745px;height:98px;background:var(--white);
    clip-path:polygon(0 0,605px 0,637px 70px,620px 98px,0 98px)}
  .contact{position:absolute;font-family:'Arimo',sans-serif;font-size:13px;color:var(--text-dark);line-height:24px}
  .contact-left{left:28px;top:20px}
  .contact-right{left:300px;top:20px}
  .contact-row{display:flex;align-items:center;gap:9px}
  .icon{width:16px;height:16px;border-radius:50%;background:var(--grey);display:inline-flex;align-items:center;justify-content:center}
  .divider{position:absolute;left:260px;top:14px;width:1px;height:70px;background:#9a9a9a}
</style>
</head>
<body>
<main class="flyer">
  <header class="header">
    <div class="brand">
      <div class="brand-mark"></div>
      <div class="brand-name"><span class="line1">Tidewell</span><span class="line2">Plumbing</span></div>
    </div>
    <div class="social"><span></span><span></span><span></span></div>
  </header>
  <svg class="header-rule" width="745" height="30" viewBox="0 0 745 30">
    <polygon points="0,0 745,0 745,6 130,6 105,28 80,6 0,6" fill="var(--yellow)"/>
  </svg>
  <div class="hero-photo" role="img" aria-label="Plumber in a hard hat operating a mini excavator beside a brick house"></div>
  <div class="hero-rule"></div>

  <div class="tile tile-trench" role="img" aria-label="Freshly dug sewer trench"></div>
  <div class="tile tile-pipe" role="img" aria-label="Sewer pipe laid in a trench"></div>
  <div class="tile tile-tap" role="img" aria-label="Chrome tap"></div>
  <div class="tile tile-sprinkler" role="img" aria-label="Garden sprinkler spraying water"></div>

  <h1 class="headline">new sewer drains to the new<br>sewer connections on<span class="accent">YOUR STREET</span></h1>
  <div class="offer-bar">Discounts for pensioners</div>
  <p class="booking">Work booked within 1 months of stamped<br>date on flyer will receive a further <span class="accent">10% off</span></p>
  <p class="reviews">We have reviews from clients that are highly<br>satisfied with our work!!</p>

  <footer class="contact-band">
    <div class="contact contact-left">
      <div class="contact-row"><span class="icon"><svg width="9" height="9" viewBox="0 0 10 10"><path d="M2 1l2 2-1 1.5c.6 1.2 1.4 2 2.5 2.5L7 6l2 2-1.3 1.5C4.5 9.3.7 5.5.5 2.3z" fill="#fff"/></svg></span>0123456789</div>
      <div class="contact-row"><span class="icon"><svg width="9" height="7" viewBox="0 0 10 7"><rect width="10" height="7" fill="#fff"/><path d="M0 0l5 4 5-4" stroke="#8c8c8c" fill="none"/></svg></span>info@tidewellplumbing.com</div>
    </div>
    <div class="divider"></div>
    <div class="contact contact-right">
      <div class="contact-row"><span class="icon"><svg width="9" height="9" viewBox="0 0 10 10"><path d="M5 1L1 5h1.5v4h5V5H9z" fill="#fff"/></svg></span>Lorem Ipsum is simply dummy</div>
      <div class="contact-row" style="padding-left:25px">of the printing typesetting industry</div>
    </div>
  </footer>
</main>
</body>
</html>
```